Quiet Harbor Advisory: Ebook Project Cover Design Needed

I recently finished writing Quiet Harbor Advisory and I need the front cover and back cover for the ebook.

I'm looking for people to want to open it based on the cover online, as I won't sell it in traditional bookstores. I'd like the ebook cover, as well as for the physical book in the 6x9 format.

```html
<!DOCTYPE html>
<html lang="en">
<head>
<meta charset="utf-8">
<title>Quiet Harbor Advisory – Ebook Cover</title>
<link rel="stylesheet" href="https://fonts.googleapis.com/css2?family=Anton&family=Cinzel:wght@600&display=swap">
<style>
  :root {
    --cover-deep: #b8320c;
    --cover-mid: #e0581a;
    --cover-glow: #f59a2c;
    --cover-light: #ffc246;
    --title-white: #ffffff;
    --author-brown: #5a1a08;
    --rim-gold: #f6b43a;
    --rim-shadow: #c5601a;
    --note-pale: #dfe6d6;
    --note-green: #7f9a86;
  }
  html, body {
    margin: 0;
    padding: 0;
    width: 802px;
    height: 1200px;
    overflow: hidden;
    background: #ffffff;
  }
  .cover {
    position: relative;
    width: 802px;
    height: 1200px;
    overflow: hidden;
    background:
      radial-gradient(ellipse 70% 55% at 50% 80%, var(--cover-light) 0%, var(--cover-glow) 30%, rgba(224,88,26,0) 75%),
      linear-gradient(200deg, var(--cover-deep) 0%, var(--cover-mid) 45%, var(--cover-glow) 100%);
  }
  .cover svg {
    position: absolute;
    left: 0;
    top: 0;
  }
  .title-line {
    font-family: "Anton", "Impact", sans-serif;
    fill: var(--title-white);
  }
  .author-name {
    font-family: "Cinzel", "Times New Roman", serif;
    font-weight: 600;
    fill: var(--author-brown);
  }
</style>
</head>
<body>
  <div class="cover">
    <svg class="torn-window" width="802" height="1200" viewBox="0 0 802 1200" role="img" aria-label="Torn opening in the cover revealing banknotes">
      <defs>
        <linearGradient id="noteFill" x1="0" y1="0" x2="1" y2="1">
          <stop offset="0" stop-color="var(--note-green)"/>
          <stop offset="0.35" stop-color="var(--note-pale)"/>
          <stop offset="0.7" stop-color="#c9d4c2"/>
          <stop offset="1" stop-color="var(--note-green)"/>
        </linearGradient>
        <linearGradient id="rimFill" x1="0" y1="0" x2="0" y2="1">
          <stop offset="0" stop-color="var(--rim-gold)"/>
          <stop offset="1" stop-color="var(--rim-shadow)"/>
        </linearGradient>
      </defs>
      <polygon class="torn-rim" fill="url(#rimFill)" points="170,720 214,690 250,660 300,640 350,624 420,630 470,622 530,632 580,640 622,668 650,690 690,712 672,760 700,820 680,880 690,940 660,1000 636,1050 600,1082 540,1070 480,1084 420,1072 360,1086 300,1064 250,1040 216,1000 184,940 200,880 174,820 192,770"/>
      <polygon class="banknotes" fill="url(#noteFill)" points="196,730 240,700 300,670 360,650 430,656 500,648 560,660 620,690 652,720 640,770 664,820 650,880 662,940 636,990 610,1040 560,1054 500,1062 430,1056 360,1064 300,1044 260,1020 232,980 210,930 222,870 200,820 214,770"/>
    </svg>

    <svg class="cover-type" width="802" height="1200" viewBox="0 0 802 1200">
      <text class="title-line title-line--top" x="152" y="284" font-size="296" textLength="508" lengthAdjust="spacingAndGlyphs">QUIET</text>
      <text class="title-line title-line--middle" x="148" y="470" font-size="165" textLength="508" lengthAdjust="spacingAndGlyphs">HARBOR</text>
      <text class="title-line title-line--bottom" x="80" y="596" font-size="110" textLength="668" lengthAdjust="spacingAndGlyphs">ADVISORY</text>
      <text class="author-name" x="172" y="1160" font-size="64" textLength="472" lengthAdjust="spacingAndGlyphs">AUTHOR NAME</text>
    </svg>
  </div>
</body>
</html>
```